International IT Business Needs a Proffesional and Innovative Business Card

We need a proffesional and innovative business card for a new company based in Venezuela called 'KorvaniLink'. We are QTB Business Partner, QTB is a key manufacture for us, one of the most influential players in technology, and the leader in cloud computing, virtualization, Big Data storage and analytics, and IT security and protection.

QTB has developed a global network of business partners to bring customers the full complement of skills and expertise required to build their information infrastructures. This partner ecosystem helps customers maximize the value of their information at the lowest total cost.

We would like to see designs that use the QTB Business Partnet logo & KorvaniLink logo.

http://brand.qtb-example.com/BrandGuide/partners/qtb-business-partner-logo/

Thank you in advance for your interest.
Updates

Happy Day!!!! I look forward to your creative design!!!

Thank you in advance.

Morna Quiroga

Target Market(s)

KorvaniLink's target markets include large companies and small- and medium-sized businesses across various vertical markets.

Industry/Entity Type

Security

Font styles to use
Other font styles liked:
• We use Meta as the QTB® corporate font.

Colors

Designer to choose colors to be used in the design.

Requirements
Must have
• Name
Title
Address
web page (www.korvani.example)

Nice to have
• Add a QR code on the reverse of the card.

```html
<!DOCTYPE html>
<html lang="en">
<head>
<meta charset="utf-8">
<title>KorvaniLink Business Card</title>
<link rel="stylesheet" href="https://fonts.googleapis.com/css2?family=Quicksand:wght@500;600;700&display=swap">
<style>
  :root {
    --backdrop: #e9e6e1;
    --card-white: #ffffff;
    --navy: #1c2f78;
    --green: #1f9a48;
    --charcoal: #3b3b3d;
    --accent-orange: #e0562e;
    --text-light: #ffffff;
    --logo-green: #2b9b3f;
  }
  * { box-sizing: border-box; margin: 0; padding: 0; }
  html, body {
    width: 1200px;
    height: 672px;
    overflow: hidden;
    background: var(--backdrop);
    font-family: "Quicksand", "Helvetica Neue", Arial, sans-serif;
  }
  .canvas {
    width: 1200px;
    height: 672px;
    display: flex;
    align-items: center;
    justify-content: center;
  }
  .card {
    width: 340px;
    height: 594px;
    background: var(--card-white);
    border-radius: 6px 6px 18px 18px;
    box-shadow: 0 6px 22px rgba(0,0,0,0.18);
    display: flex;
    flex-direction: column;
    overflow: hidden;
    position: relative;
  }
  .top-strip {
    flex: none;
    height: 22px;
    margin: 0 10px;
    background: var(--navy);
    border-radius: 0 0 12px 12px;
  }
  .logo-area {
    flex: 0 0 168px;
    display: flex;
    align-items: center;
    justify-content: center;
    gap: 10px;
  }
  .logo-dot {
    width: 16px;
    height: 16px;
    border-radius: 50%;
    background: var(--logo-green);
  }
  .logo-name {
    font-size: 34px;
    font-weight: 700;
    color: var(--navy);
    letter-spacing: -0.5px;
  }
  .identity {
    flex: none;
    background: var(--navy);
    border-radius: 16px 16px 0 0;
    padding: 22px 24px 18px;
    text-align: center;
    color: var(--text-light);
    border-bottom: 3px solid var(--accent-orange);
  }
  .identity .person-name {
    font-size: 20px;
    font-weight: 600;
    letter-spacing: 1.5px;
    text-transform: uppercase;
  }
  .identity .person-title {
    font-size: 13px;
    font-weight: 600;
    letter-spacing: 1.6px;
    text-transform: uppercase;
    margin-top: 2px;
  }
  .contacts {
    background: var(--charcoal);
    flex: 1;
    padding: 20px 0 30px 92px;
    display: flex;
    flex-direction: column;
    justify-content: space-between;
    list-style: none;
    color: var(--text-light);
  }
  .contact-row {
    display: flex;
    align-items: center;
    gap: 10px;
    font-size: 13px;
    font-weight: 500;
    letter-spacing: 0.6px;
    line-height: 1.2;
  }
  .contact-icon {
    width: 20px;
    height: 20px;
    flex: none;
  }
  .address-band {
    flex: none;
    background: var(--green);
    border-radius: 16px 16px 18px 18px;
    margin-top: -12px;
    padding: 24px 24px 26px 70px;
    display: flex;
    align-items: center;
    gap: 12px;
    color: var(--text-light);
    font-size: 13px;
    font-weight: 600;
    letter-spacing: 0.5px;
    line-height: 1.45;
    position: relative;
  }
  .address-icon { width: 24px; height: 24px; flex: none; }
  .address-text { font-style: normal; }
</style>
</head>
<body>
<main class="canvas">
  <article class="card">
    <div class="top-strip"></div>

    <header class="logo-area">
      <span class="logo-dot"></span>
      <span class="logo-name">KorvaniLink</span>
    </header>

    <section class="identity">
      <p class="person-name">Davin Orrel</p>
      <p class="person-title">General Manager</p>
    </section>

    <ul class="contacts">
      <li class="contact-row">
        <svg class="contact-icon" viewBox="0 0 20 20" aria-hidden="true">
          <circle cx="10" cy="10" r="9" fill="none" stroke="#fff" stroke-width="1.4"/>
          <path d="M7 5.5l1.6 0 .8 2.2-1 .9c.6 1.3 1.5 2.2 2.8 2.8l.9-1 2.2.8v1.6c0 .6-.6 1-1.2.9C9.6 13.3 6.7 10.4 6.1 6.9 6 6.2 6.4 5.5 7 5.5z" fill="#fff"/>
        </svg>
        <span>010 555 0147</span>
      </li>
      <li class="contact-row">
        <svg class="contact-icon" viewBox="0 0 20 20" aria-hidden="true">
          <circle cx="10" cy="10" r="9" fill="none" stroke="#fff" stroke-width="1.4"/>
          <rect x="7" y="4.5" width="6" height="11" rx="1.2" fill="#fff"/>
          <rect x="8" y="6" width="4" height="6.5" fill="#3b3b3d"/>
        </svg>
        <span>010 555 0147</span>
      </li>
      <li class="contact-row">
        <svg class="contact-icon" viewBox="0 0 20 20" aria-hidden="true">
          <circle cx="10" cy="10" r="9" fill="none" stroke="#fff" stroke-width="1.4"/>
          <rect x="7" y="5" width="6" height="3.5" fill="#fff"/>
          <rect x="5" y="8.5" width="10" height="4.5" rx="1" fill="#fff"/>
          <rect x="7" y="12" width="6" height="3" fill="#fff" stroke="#3b3b3d" stroke-width="0.6"/>
        </svg>
        <span>010 555 0147</span>
      </li>
      <li class="contact-row">
        <svg class="contact-icon" viewBox="0 0 20 20" aria-hidden="true">
          <circle cx="10" cy="10" r="9" fill="none" stroke="#fff" stroke-width="1.4"/>
          <rect x="5" y="6.5" width="10" height="7" rx="1" fill="#fff"/>
          <path d="M5.5 7l4.5 3.5L14.5 7" fill="none" stroke="#3b3b3d" stroke-width="1"/>
        </svg>
        <span>hello@korvani.example</span>
      </li>
      <li class="contact-row">
        <svg class="contact-icon" viewBox="0 0 20 20" aria-hidden="true">
          <circle cx="10" cy="10" r="9" fill="none" stroke="#fff" stroke-width="1.4"/>
          <circle cx="10" cy="10" r="5" fill="none" stroke="#fff" stroke-width="1"/>
          <ellipse cx="10" cy="10" rx="2.2" ry="5" fill="none" stroke="#fff" stroke-width="1"/>
          <line x1="5" y1="10" x2="15" y2="10" stroke="#fff" stroke-width="1"/>
        </svg>
        <span>www.korvani.example</span>
      </li>
    </ul>

    <footer class="address-band">
      <svg class="address-icon" viewBox="0 0 24 24" aria-hidden="true">
        <circle cx="12" cy="12" r="11" fill="none" stroke="#fff" stroke-width="1.5"/>
        <path d="M12 5.5a4 4 0 0 0-4 4c0 3 4 8 4 8s4-5 4-8a4 4 0 0 0-4-4z" fill="#fff"/>
        <circle cx="12" cy="9.6" r="1.5" fill="#1f9a48"/>
      </svg>
      <address class="address-text">42 Vale Crest Road<br>Block 5, Marren Lane</address>
    </footer>
  </article>
</main>
</body>
</html>
```